Bref créative
Thriving Neighbors of Alder Valley
Professional
This is a TEMPLATE for a card that will be used for many, many people, thus we need a design that allows us a template format that can be input with all the standard info, title, address, phone, cell, fax, email and web address.
Please use a template format that so that we can change card to various people

```html
<!DOCTYPE html>
<html lang="en">
<head>
<meta charset="utf-8">
<title>Thriving Neighbors of Alder Valley – Stationery</title>
<link href="https://fonts.googleapis.com/css2?family=Open+Sans:wght@400;700;800&display=swap" rel="stylesheet">
<style>
:root{
  --stage:#3b3b3d;
  --paper:#ffffff;
  --green:#2f8f3c;
  --green-dark:#1d6a2a;
  --navy:#15233f;
  --ink:#3a3a3a;
  --muted:#9a9a9a;
  --caption:#c9c9c9;
}
*{margin:0;padding:0;box-sizing:border-box}
html,body{width:1200px;height:343px;overflow:hidden;background:var(--stage);font-family:"Open Sans",Arial,sans-serif}
.stage{position:relative;width:1200px;height:343px}
.piece{position:absolute;background:var(--paper);overflow:hidden;box-shadow:0 2px 6px rgba(0,0,0,.45)}
.swoosh{position:absolute;left:0;bottom:0;width:100%}
.brand{display:flex;align-items:center;gap:4px;color:var(--green);font-weight:800;line-height:1.1}
.brand-mark{background:var(--green);flex:none}
.caption{position:absolute;color:var(--caption);font-size:6px;letter-spacing:.2px}
.contact{color:var(--muted);font-size:4px;line-height:1.5;text-align:right}

/* identity block */
.identity{position:absolute;left:14px;top:12px;width:150px;display:flex;flex-direction:column;align-items:center;gap:6px}
.identity .brand-mark{width:40px;height:40px;border-radius:6px}
.identity-name{color:#fff;font-weight:800;font-size:9px;text-align:center;line-height:1.2}

.card{width:150px;height:48px;left:14px}
.card-front{top:132px}
.card-back{top:240px;display:flex;align-items:center;justify-content:center}
.card-front .brand{position:absolute;left:8px;top:6px;font-size:5.5px}
.card-front .brand-mark{width:8px;height:8px}
.card-person{position:absolute;left:8px;top:20px;font-size:4.5px;color:var(--ink);font-weight:700}
.card-person span{display:block;font-weight:400;color:var(--muted);font-size:3.5px}
.card-front .contact{position:absolute;right:8px;top:6px;font-size:3.5px}
.card-back .brand{font-size:6.5px}
.card-back .brand-mark{width:10px;height:10px}

.letterhead{top:12px;width:216px;height:312px}
.letterhead.one{left:168px}
.letterhead.two{left:408px}
.letterhead .brand{position:absolute;left:16px;top:12px;font-size:6.5px;width:90px}
.letterhead .brand-mark{width:12px;height:12px}
.letterhead .contact{position:absolute;right:16px;top:12px}

.envelope{left:636px;width:252px;height:100px}
.envelope.one{top:67px}
.envelope.two{top:204px}
.envelope .brand{position:absolute;left:12px;top:10px;font-size:6.5px;width:90px}
.envelope .brand-mark{width:12px;height:12px}

.back{width:280px;height:100px}
.back.navy{left:908px;top:62px;background:var(--navy)}
.back.green{left:912px;top:130px;background:var(--green)}
.back.white{left:900px;top:210px}
.back svg{position:absolute;inset:0;width:100%;height:100%}
.back .brand-mark{position:absolute;left:130px;top:24px;width:20px;height:20px;background:#fff;border-radius:2px}
</style>
</head>
<body>
<main class="stage">

  <section class="identity">
    <div class="brand-mark"></div>
    <div class="identity-name">Thriving Neighbors of Alder Valley</div>
  </section>

  <article class="piece card card-front">
    <div class="brand"><span class="brand-mark"></span>Thriving Neighbors<br>of Alder Valley</div>
    <div class="card-person">Jordan Ellis<span>Program Coordinator</span></div>
    <div class="contact">1420 Cedar Row<br>Alder Valley, WA 98400<br>(253) 555-0142<br>info@thrivingalder.org</div>
    <svg class="swoosh" viewBox="0 0 150 14" height="14" preserveAspectRatio="none" aria-hidden="true">
      <path d="M0 7 Q75 -2 150 5 L150 14 L0 14Z" fill="var(--green)"/>
      <path d="M0 10 Q75 2 150 8 L150 14 L0 14Z" fill="var(--navy)"/>
    </svg>
  </article>

  <article class="piece card card-back">
    <div class="brand"><span class="brand-mark"></span>Thriving Neighbors of Alder Valley</div>
  </article>

  <article class="piece letterhead one">
    <div class="brand"><span class="brand-mark"></span>Thriving Neighbors of Alder Valley</div>
    <div class="contact">1420 Cedar Row, Alder Valley, WA 98400<br>(253) 555-0142<br>thrivingalder.org</div>
    <svg class="swoosh" viewBox="0 0 216 40" height="40" preserveAspectRatio="none" aria-hidden="true">
      <path d="M0 18 Q108 0 216 14 L216 40 L0 40Z" fill="var(--green)"/>
      <path d="M0 26 Q108 10 216 22 L216 40 L0 40Z" fill="var(--green-dark)"/>
      <path d="M0 32 Q108 18 216 30 L216 40 L0 40Z" fill="var(--navy)"/>
    </svg>
  </article>

  <article class="piece letterhead two">
    <div class="brand"><span class="brand-mark"></span>Thriving Neighbors of Alder Valley</div>
    <div class="contact">1420 Cedar Row, Alder Valley, WA 98400<br>(253) 555-0142<br>thrivingalder.org</div>
    <svg class="swoosh" viewBox="0 0 216 40" height="40" preserveAspectRatio="none" aria-hidden="true">
      <path d="M0 18 Q108 0 216 14 L216 40 L0 40Z" fill="var(--green)"/>
      <path d="M0 26 Q108 10 216 22 L216 40 L0 40Z" fill="var(--green-dark)"/>
      <path d="M0 32 Q108 18 216 30 L216 40 L0 40Z" fill="var(--navy)"/>
    </svg>
  </article>

  <article class="piece envelope one">
    <div class="brand"><span class="brand-mark"></span>Thriving Neighbors of Alder Valley</div>
    <svg class="swoosh" viewBox="0 0 252 26" height="26" preserveAspectRatio="none" aria-hidden="true">
      <path d="M0 12 Q126 0 252 8 L252 26 L0 26Z" fill="var(--green)"/>
      <path d="M0 19 Q126 7 252 15 L252 26 L0 26Z" fill="var(--navy)"/>
    </svg>
  </article>
  <p class="caption" style="left:636px;top:170px">Envelope front</p>

  <article class="piece envelope two">
    <div class="brand"><span class="brand-mark"></span>Thriving Neighbors of Alder Valley</div>
    <svg class="swoosh" viewBox="0 0 252 26" height="26" preserveAspectRatio="none" aria-hidden="true">
      <path d="M0 12 Q126 0 252 8 L252 26 L0 26Z" fill="var(--green)"/>
      <path d="M0 19 Q126 7 252 15 L252 26 L0 26Z" fill="var(--navy)"/>
    </svg>
  </article>
  <p class="caption" style="left:636px;top:307px">Envelope back</p>

  <article class="piece back navy">
    <svg viewBox="0 0 280 100" preserveAspectRatio="none" aria-hidden="true">
      <path d="M0 0 L140 58 L280 0" fill="none" stroke="rgba(255,255,255,.15)" stroke-width="1"/>
    </svg>
    <span class="brand-mark"></span>
  </article>

  <article class="piece back green">
    <svg viewBox="0 0 280 100" preserveAspectRatio="none" aria-hidden="true">
      <path d="M0 0 L140 56 L280 0" fill="var(--green-dark)"/>
      <path d="M0 100 L126 48 M280 100 L154 48" stroke="rgba(0,0,0,.15)" stroke-width="1"/>
    </svg>
  </article>

  <article class="piece back white">
    <svg viewBox="0 0 280 100" preserveAspectRatio="none" aria-hidden="true">
      <path d="M0 0 L140 58 L280 0" fill="#f1f1f1" stroke="#d6d6d6" stroke-width="1"/>
      <path d="M0 100 L126 50 M280 100 L154 50" stroke="#dcdcdc" stroke-width="1"/>
    </svg>
  </article>

</main>
</body>
</html>
```